Vorlisk.com Redesign

Please read the notes and see the site-map attached.
Updates

We are looking for something highly creative. Please provide your best work. Best of luck and thank you very much for your hard work!

Project Deadline Extended
Reason: I am seeing good designs but I am not seeing great designs. I really need a design that is unique and is going to wow me. No one is required to stick to the existing color schemes etc. You are free to use other colors etc. I am seeing a lot of the same colors that are used on the site now.

Target Market(s)

Business and entrepreneurs mainly. People looking to build applications, software or launch web or mobile tech products.

Colors

Designer to choose colors to be used in the design.

Requirements
Must have
• See my attached html file.
Nice to have
Should not have
• No sure

```html
<!DOCTYPE html>
<html lang="en">
<head>
<meta charset="utf-8">
<title>Vorlisk.com</title>
<link rel="stylesheet" href="https://fonts.googleapis.com/css2?family=Ubuntu:wght@300;400;500;700&family=Open+Sans:ital,wght@0,400;0,600;0,700;1,400&display=swap">
<style>
:root{
  --green:#6cb33f;
  --green-light:#8fd14f;
  --green-dark:#2f5a12;
  --navy:#1b3f5a;
  --navy-deep:#183a50;
  --ink:#333;
  --grey-bg:#f3f3f3;
  --dark-bar:#2b2b2b;
  --rule:#35576e;
  --link:#7ec3ff;
}
*{margin:0;padding:0;box-sizing:border-box}
html,body{width:852px;height:1200px;overflow:hidden;background:#fff}
body{position:relative;font-family:"Open Sans",sans-serif;color:var(--ink)}
.abs{position:absolute}

/* top bar */
.top-bar{left:0;top:0;width:852px;height:33px;background:#f7f7f7;border-top:3px solid var(--green);border-bottom:1px solid #ddd;font-size:7.5px;color:#666}
.top-bar .item{position:absolute;top:11px;display:flex;align-items:center;gap:6px}
.corner-plus{right:1px;top:-3px;width:22px;height:18px;border-radius:0 0 0 11px;background:var(--green);color:#fff;font-size:10px;text-align:center;line-height:14px}

/* header */
.site-header{left:0;top:33px;width:852px;height:71px;background:linear-gradient(#fff,#f1f1f1);border-bottom:4px solid var(--green)}
.brand{left:100px;top:20px;display:flex;align-items:center;gap:8px}
.brand-dot{width:24px;height:24px;border-radius:50%;background:var(--navy)}
.brand-name{font-family:"Ubuntu",sans-serif;font-size:22px;font-weight:500;color:var(--navy)}
.main-nav{left:478px;top:38px;display:flex;gap:7px;font-size:7.8px;color:#444;align-items:center}
.main-nav a{text-decoration:none;color:inherit;padding:2px 5px}
.main-nav a.active{background:var(--navy);color:#fff}

/* hero */
.hero{left:0;top:108px;width:852px;height:281px;background:radial-gradient(ellipse at 70% 40%,#6b4634 0%,#3a2218 45%,#1c0f0a 100%)}
.hero-kicker{left:100px;top:57px;font-family:"Ubuntu",sans-serif;font-weight:700;font-size:19px;color:#fff}
.hero-title{left:100px;top:76px;font-family:"Ubuntu",sans-serif;font-weight:700;font-size:40px;color:#fff;letter-spacing:.5px}
.hero-rule{left:100px;top:124px;width:315px;height:3px;background:var(--green)}
.hero-copy{left:100px;top:136px;width:320px;font-size:11.5px;line-height:16px;color:#eee;text-transform:uppercase}
.mascot{left:326px;top:46px;width:90px;height:72px;border-radius:6px;background:linear-gradient(#6c4e40,#4a3226);opacity:.8}
.btn-green{background:linear-gradient(var(--green-light),var(--green));color:#fff;border:2px solid #4a8a22;border-radius:4px;text-align:center;box-shadow:0 1px 2px rgba(0,0,0,.4)}
.hero-btn{left:99px;top:189px;width:102px;height:30px;font-size:8.5px;line-height:26px}
.hero-visual{left:411px;top:67px;width:341px;height:177px;border-radius:6px;background:linear-gradient(135deg,#cfcfd4 0%,#5a4d8a 30%,#2d2a55 60%,#b9b9be 100%)}
.slider-dots{display:flex;gap:3px}
.slider-dots span{width:11px;height:11px;background:#fff;border:1px solid #ccc}
.slider-dots span.on{background:var(--green)}
.hero-dots{left:399px;top:260px}

/* promo bar */
.promo-bar{left:0;top:389px;width:852px;height:56px;background:var(--dark-bar)}
.promo-text{left:100px;top:24px;font-size:8.6px;color:#eee}
.promo-btn{left:564px;top:15px;width:189px;height:31px;font-size:12px;line-height:27px}

/* services */
.services{left:0;top:461px;width:852px;height:262px;background:var(--grey-bg);border-top:1px solid #e2e2e2}
.section-tab{left:345px;top:0;width:155px;height:38px;font-family:"Ubuntu",sans-serif;font-weight:700;font-size:16px;line-height:36px;border-radius:0 0 3px 3px;border-top:none}
.service-icon{width:124px;height:124px;border-radius:50%;background:var(--navy);border:2px solid #102a3d;box-shadow:0 10px 10px -4px rgba(0,0,0,.25);display:flex;align-items:center;justify-content:center}
.service-icon.featured{background:var(--green);border-color:#4f8f26}
.service-label{width:150px;text-align:center;font-family:"Ubuntu",sans-serif;font-weight:300;font-size:12px;line-height:14.5px;color:#444;text-transform:uppercase}
.service-band{left:0;top:723px;width:852px;height:23px;background:linear-gradient(90deg,var(--navy) 0%,#2c5a5a 40%,var(--green) 100%)}

/* testimonials */
.testimonials{left:100px;top:753px;width:653px;height:229px;border:1px solid #ccc;background:#fff}
.testimonials-head{left:0;top:0;width:651px;height:29px;background:var(--navy);color:#fff;font-family:"Ubuntu",sans-serif;font-weight:700;font-size:18px;line-height:30px;padding-left:15px}
.quote{left:16px;width:619px;font-style:italic;font-size:11.5px;line-height:14.5px;color:#333}
.quote-rule{left:16px;width:619px;height:1px;background:#bbb}
.quote-author{left:16px;font-style:italic;font-size:11.5px;color:#333}
.testi-dots{left:583px;top:213px}
.testi-dots span{width:10px;height:10px}

/* footer */
.site-footer{left:0;top:990px;width:852px;height:170px;background:var(--navy-deep)}
.foot-heading{top:17px;font-family:"Ubuntu",sans-serif;font-size:10px;font-weight:700;color:var(--green-light);line-height:12px}
.foot-rule{top:45px;width:92px;height:1px;background:var(--rule)}
.foot-body{top:58px;font-size:7.4px;line-height:9.5px;color:#fff;text-transform:uppercase;list-style:none}
.foot-body li::before{content:"-\00a0\00a0"}
.foot-body a{color:var(--link)}
.read-more{top:1135px;font-size:7.8px;color:var(--link);text-decoration:underline}
.read-more.green{color:var(--green-light)}
.foot-arrows{left:716px;top:16px;display:flex;gap:3px}
.foot-arrows span{width:17px;height:14px;display:flex;align-items:center;justify-content:center}
.map{left:539px;top:58px;width:107px;height:66px;background:linear-gradient(135deg,#e8e4d8,#d9d5c6 60%,#b9d3e4);border:1px solid #fff}
.address{left:653px;top:58px;font-size:7.4px;line-height:9.5px;color:#fff}
.address .co{color:var(--link);display:block;margin-bottom:8px}

/* bottom bar */
.bottom-bar{left:0;top:1160px;width:852px;height:40px;background:linear-gradient(var(--green-light),var(--green))}
.copyright{left:100px;top:15px;font-family:"Ubuntu",sans-serif;font-size:10px;font-weight:700;color:var(--green-dark)}
</style>
</head>
<body>

<div class="abs top-bar">
  <div class="item" style="left:100px">
    <svg width="10" height="9" viewBox="0 0 10 9"><path d="M1 6 V4 a4 4 0 0 1 8 0 V6" fill="none" stroke="#777" stroke-width="1.2"/><rect x="0.5" y="5" width="2" height="3.5" fill="#777"/><rect x="7.5" y="5" width="2" height="3.5" fill="#777"/></svg>
    +1 (555) 014-2290
  </div>
  <div class="item" style="left:205px">
    <svg width="12" height="9" viewBox="0 0 12 9"><rect x=".5" y=".5" width="11" height="8" fill="none" stroke="#777"/><path d="M.5 .5 L6 5 L11.5 .5" fill="none" stroke="#777"/></svg>
    hello@vorlisk.com
  </div>
  <div class="item" style="left:614px">
    <svg width="7" height="9" viewBox="0 0 7 9"><circle cx="3.5" cy="2.5" r="2.2" fill="#777"/><path d="M0 9 a3.5 3.5 0 0 1 7 0z" fill="#777"/></svg>
    Client Login
  </div>
  <div class="item" style="left:687px">
    <svg width="15" height="9" viewBox="0 0 15 9"><ellipse cx="5" cy="4" rx="5" ry="3.5" fill="#777"/><ellipse cx="10.5" cy="5.5" rx="4.5" ry="3.2" fill="#999"/></svg>
    Live Chat
  </div>
  <div class="abs corner-plus">+</div>
</div>

<header class="abs site-header">
  <div class="abs brand"><span class="brand-dot"></span><span class="brand-name">vorlisk</span></div>
  <nav class="abs main-nav">
    <a class="active">HOME</a><a>ABOUT US</a><a>WHAT WE DO</a><a>OUR WORK</a><a>BLOG</a><a>REACH US</a>
  </nav>
</header>

<section class="abs hero">
  <div class="abs hero-kicker">CLIENT FOR LIFE</div>
  <div class="abs hero-title">APPROACH</div>
  <div class="abs mascot" role="img" aria-label="Line illustration of a meditating figure with sparkles"></div>
  <div class="abs hero-rule"></div>
  <p class="abs hero-copy">Our mantra is to earn the trust and respect of our clients and keep that trust.</p>
  <div class="abs btn-green hero-btn">VIEW MORE</div>
  <div class="abs hero-visual" role="img" aria-label="Laptop and smartphone showing client website projects"></div>
  <div class="abs slider-dots hero-dots"><span></span><span></span><span></span><span class="on"></span></div>
</section>

<div class="abs promo-bar">
  <p class="abs promo-text">LOREM IPSUM IS SIMPLY DUMMY TEXT. LOREM IPSUM IS SIMPLY DUMMY TEXT.</p>
  <div class="abs btn-green promo-btn">DOWNLOAD BROCHURE</div>
</div>

<section class="abs services">
  <div class="abs btn-green section-tab">OUR SERVICES</div>

  <div class="abs service-icon" style="left:129px;top:69px">
    <svg width="56" height="48" viewBox="0 0 56 48" fill="none" stroke="#fff" stroke-width="3"><rect x="3" y="10" width="38" height="30" rx="4"/><line x1="3" y1="18" x2="41" y2="18"/><circle cx="9" cy="14" r="1" fill="#fff"/><circle cx="14" cy="14" r="1" fill="#fff"/><path d="M24 34 L50 6" stroke-width="5" stroke-linecap="round"/></svg>
  </div>
  <div class="abs service-icon featured" style="left:286px;top:69px">
    <svg width="50" height="50" viewBox="0 0 50 50" fill="none" stroke="#fff" stroke-width="3"><rect x="6" y="4" width="16" height="28" rx="3"/><circle cx="14" cy="26" r="1.5" fill="#fff"/><path d="M26 14 H40 a4 4 0 0 1 4 4 V40 a4 4 0 0 1 -4 4 H18 a4 4 0 0 1 -4 -4 V36"/></svg>
  </div>
  <div class="abs service-icon" style="left:442px;top:69px">
    <svg width="52" height="50" viewBox="0 0 52 50" fill="none" stroke="#fff" stroke-width="3"><circle cx="16" cy="16" r="8"/><circle cx="16" cy="16" r="3" fill="#fff"/><g stroke-width="3.5"><line x1="16" y1="2" x2="16" y2="6"/><line x1="16" y1="26" x2="16" y2="30"/><line x1="2" y1="16" x2="6" y2="16"/><line x1="26" y1="16" x2="30" y2="16"/><line x1="6" y1="6" x2="9" y2="9"/><line x1="23" y1="23" x2="26" y2="26"/><line x1="26" y1="6" x2="23" y2="9"/><line x1="6" y1="26" x2="9" y2="23"/></g><path d="M32 12 H44 a4 4 0 0 1 4 4 V42 a4 4 0 0 1 -4 4 H20 a4 4 0 0 1 -4 -4 V36"/></svg>
  </div>
  <div class="abs service-icon" style="left:600px;top:69px">
    <svg width="50" height="50" viewBox="0 0 50 50" fill="none" stroke="#fff" stroke-width="3"><circle cx="18" cy="12" r="7" fill="#fff"/><path d="M4 28 a14 8 0 0 1 28 0z" fill="#fff"/><path d="M30 16 H40 a4 4 0 0 1 4 4 V40 a4 4 0 0 1 -4 4 H18 a4 4 0 0 1 -4 -4 V34"/></svg>
  </div>

  <p class="abs service-label" style="left:115px;top:211px">Web<br>Development</p>
  <p class="abs service-label" style="left:273px;top:211px">Mobile App<br>Development</p>
  <p class="abs service-label" style="left:436px;top:211px">Custom Software<br>Development</p>
  <p class="abs service-label" style="left:580px;top:211px">User Experience<br>Design</p>
</section>
<div class="abs service-band"></div>

<section class="abs testimonials">
  <h2 class="abs testimonials-head">WHY CLIENTS LOVE US!</h2>
  <p class="abs quote" style="top:49px">We sought after a really creative and one of a kind web presence and that’s exactly what creators at Vorlisk designed for us. The Vorlisk team were a pleasure to work with and they are always quick to respond with solutions. We are very pleased with their work and dedication to their clients!!!</p>
  <div class="abs quote-rule" style="top:98px"></div>
  <p class="abs quote-author" style="top:102px">Marla Quintero-Hale, Co-Founder-Brightpath.io</p>
  <p class="abs quote" style="top:141px">After moving CoatLine to Vorlisk things really started to take form and today I can honestly say my expectations have been surpassed. I look forward to working with Vorlisk as we reinvent software for the powder coating industry.</p>
  <div class="abs quote-rule" style="top:191px"></div>
  <p class="abs quote-author" style="top:195px">Devan Arroway, CEO-CoatLine Inc</p>
  <div class="abs slider-dots testi-dots"><span></span><span></span><span></span><span class="on"></span></div>
</section>

<footer class="abs site-footer">
  <h3 class="abs foot-heading" style="left:100px">WHO WE ARE ?</h3>
  <div class="abs foot-rule" style="left:100px"></div>
  <p class="abs foot-body" style="left:100px">We are a close knit<br>team of designers<br>and developers<br>who specialize in<br>web, mobile and<br>custom application<br>development<br>services.</p>

  <h3 class="abs foot-heading" style="left:233px">WHAT WE DO ?</h3>
  <div class="abs foot-rule" style="left:233px"></div>
  <ul class="abs foot-body" style="left:233px"><li>Web development</li><li>Mobile application</li><li>Development</li><li>Custom software</li><li>Development</li><li>User experience design</li></ul>

  <h3 class="abs foot-heading" style="left:389px">OUR WORK /<br>CASE STUDIES</h3>
  <div class="abs foot-rule" style="left:389px;width:104px"></div>
  <ul class="abs foot-body" style="left:389px"><li>Image gallery</li><li>Testimonial</li><li><a>Download</a> our profile</li><li>Videos</li></ul>

  <h3 class="abs foot-heading" style="left:539px">REACH US</h3>
  <div class="abs foot-rule" style="left:539px;width:214px"></div>
  <div class="abs foot-arrows">
    <span style="background:#ddd"><svg width="6" height="8"><path d="M5 0 L1 4 L5 8" fill="none" stroke="#333" stroke-width="1.5"/></svg></span>
    <span style="background:#111"><svg width="6" height="8"><path d="M1 0 L5 4 L1 8" fill="none" stroke="#fff" stroke-width="1.5"/></svg></span>
  </div>
  <div class="abs map" role="img" aria-label="Map showing the office region"></div>
  <p class="abs address"><span class="co">VORLISK LLC</span>2210 HARBOR PARK AVE #40<br>LAKEMONT, CA 90000</p>
</footer>
<a class="abs read-more" style="left:100px">READ MORE</a>
<a class="abs read-more" style="left:241px">READ MORE</a>
<a class="abs read-more" style="left:399px">READ MORE</a>
<a class="abs read-more green" style="left:542px">READ MORE</a>

<div class="abs bottom-bar">
  <p class="abs copyright">Copyright 2014 All Right Reserved</p>
</div>

</body>
</html>
```